Marcus Doyle 'only so far' CD cover design

Design a CD cover and a logo (using my initials- MD)
Basically the two files attached are what I'm looking for (front and back)
I'd like my image to stand out with a white background.
The logo will be something I use on all my albums and website.
I like the white bold look.
Possible enhance image marginally I've lost a little weight since taking the picture.
The music I perform is Jazz Swing

Jazz Swing Audience

```html
<!DOCTYPE html>
<html lang="en">
<head>
<meta charset="utf-8">
<title>Marcus Doyle – Only So Far</title>
<link rel="stylesheet" href="https://fonts.googleapis.com/css2?family=Limelight&family=Federo&family=Poiret+One&display=swap">
<style>
  :root {
    --stage: #808080;
    --cover: #ffffff;
    --ink: #000000;
    --title-grey: #7a7a7a;
    --photo-top: #e9e4e1;
    --photo-mid: #8f8580;
    --photo-bottom: #1a1a1a;
  }
  html, body {
    margin: 0;
    padding: 0;
    width: 1200px;
    height: 1000px;
    overflow: hidden;
    background: var(--stage);
  }
  .canvas {
    position: relative;
    width: 1200px;
    height: 1000px;
    background: var(--stage);
  }
  .cd-cover {
    position: absolute;
    left: 245px;
    top: 145px;
    width: 708px;
    height: 708px;
    background: var(--cover);
    overflow: hidden;
  }
  .artist-portrait {
    position: absolute;
    left: 155px;
    top: 170px;
    width: 553px;
    height: 538px;
    background: linear-gradient(180deg, var(--photo-top) 0%, var(--photo-mid) 45%, var(--photo-bottom) 75%, var(--photo-bottom) 100%);
  }
  .artist-name {
    position: absolute;
    left: 26px;
    top: 52px;
    margin: 0;
    font-family: "Limelight", sans-serif;
    font-weight: 400;
    font-size: 90px;
    line-height: 1;
    letter-spacing: 1px;
    color: var(--ink);
    white-space: nowrap;
  }
  .monogram {
    position: absolute;
    left: 28px;
    top: 150px;
    margin: 0;
    font-family: "Limelight", sans-serif;
    font-weight: 400;
    font-size: 40px;
    line-height: 1;
    color: var(--ink);
  }
  .album-title {
    position: absolute;
    left: 24px;
    top: 318px;
    margin: 0;
    color: var(--title-grey);
    font-weight: 400;
  }
  .album-title .line {
    display: block;
    font-family: "Federo", sans-serif;
    font-size: 72px;
    line-height: 78px;
    letter-spacing: 22px;
  }
  .album-title .line-big {
    display: block;
    margin-top: -13px;
    font-family: "Poiret One", sans-serif;
    font-size: 225px;
    line-height: 225px;
    letter-spacing: -4px;
    opacity: 0.85;
  }
</style>
</head>
<body>
<main class="canvas">
  <section class="cd-cover">
    <div class="artist-portrait" role="img" aria-label="Portrait photo of the singer in a black suit, white shirt and black tie"></div>

    <h1 class="artist-name">Marcus Doyle</h1>

    <p class="monogram">MD</p>

    <h2 class="album-title">
      <span class="line">ONLY</span>
      <span class="line">SO</span>
      <span class="line-big">FAR</span>
    </h2>
  </section>
</main>
</body>
</html>
```